Upmarket cover for top management book, ideally unlike most common cover pages

This book is about both good management and mismanagement and introduces novel concepts such as the inverse exponential law in strategy, No doubt that these concepts will be criticized by some management scholars. However, students, a few other colleagues and key top managers find the new ideas useful and eye-opening.
The cover must help communicate a deeper vision of management as an expression of life creation and a sort of "divine" energy.

Practical details:
Print and ebook cover page plus elements of the cover for each of the three main book sections.
Title; The Orchard
Subtitle: Harvest methods and the spiral rising rule
Author: Teodor B. Malvezzi
Publisher: Quillstone Author Press
Width x height: 13,97 x 21,59 cm (without bleed)
Spine: 14-15 cm according to paper color

Target Market(s)

Mostly managers who did not have the opportunity of attending postgraduate management studies such as the MBA

Industry/Entity Type

Mostly high technology

Font styles to use
Serif
Sans Serif
Other font styles liked:
• Arial nova, Arial light

Requirements
Must have
• Preferably cover and back cover on white background, but any good proposals would do.
Nice to have
• An image of bright and reassuring, albeit potentially unlimited, strength. Ideally the cover design should show that good management is good for the COMMON GOOD of society
Should not have
• Please do not show images of people and no proposals reminiscent of other management and strategy book covers

```html
<!DOCTYPE html>
<html lang="en">
<head>
<meta charset="utf-8">
<title>The Orchard – Book Cover</title>
<link rel="stylesheet" href="https://fonts.googleapis.com/css2?family=Bebas+Neue&family=Lato:wght@400&display=swap">
<style>
  :root {
    --stage-grey: #939393;
    --wall-light: #f3f4f5;
    --wall-shade: #e2e4e6;
    --board-top: #2c2c2c;
    --board-bottom: #0c0c0c;
    --gold-deep: #a8772a;
    --gold-mid: #c99a3e;
    --gold-bright: #e7c652;
    --ink: #1b1b1d;
    --paper: #ffffff;
  }
  * { margin: 0; padding: 0; box-sizing: border-box; }
  html, body {
    width: 1200px;
    height: 1200px;
    overflow: hidden;
    background: var(--stage-grey);
  }
  .book-cover {
    position: absolute;
    left: 236px;
    top: 54px;
    width: 728px;
    height: 1091px;
    overflow: hidden;
  }
  .wall-and-board {
    position: absolute;
    inset: 0;
    background: linear-gradient(180deg,
      var(--wall-light) 0%,
      var(--wall-shade) 77.4%,
      var(--board-top) 77.5%,
      var(--board-bottom) 100%);
  }
  .king-photo {
    position: absolute;
    left: 273px;
    top: 511px;
    width: 185px;
    height: 466px;
    border-radius: 60px 60px 28px 28px;
    background: linear-gradient(90deg,
      var(--gold-deep) 0%,
      var(--gold-bright) 45%,
      var(--gold-mid) 75%,
      var(--gold-deep) 100%);
  }
  .title-small,
  .title-large {
    position: absolute;
    left: 0;
    width: 100%;
    text-align: center;
    font-family: "Bebas Neue", "Oswald", sans-serif;
    line-height: 1;
    background: linear-gradient(90deg, var(--gold-deep) 0%, var(--gold-bright) 50%, var(--gold-deep) 100%);
    -webkit-background-clip: text;
    background-clip: text;
    color: transparent;
  }
  .title-small {
    top: 66px;
    font-size: 100px;
  }
  .title-large {
    top: 140px;
    font-size: 204px;
    letter-spacing: 0.01em;
  }
  .subtitle {
    position: absolute;
    left: 40px;
    right: 40px;
    top: 328px;
    text-align: center;
    font-family: "Lato", "Arial", sans-serif;
    font-weight: 400;
    font-size: 36px;
    line-height: 40px;
    color: var(--ink);
  }
  .author {
    position: absolute;
    left: 0;
    width: 100%;
    top: 1014px;
    text-align: center;
    font-family: "Bebas Neue", "Oswald", sans-serif;
    font-size: 52px;
    line-height: 1;
    letter-spacing: 0.4em;
    text-indent: 0.4em;
    color: var(--paper);
  }
</style>
</head>
<body>
  <main class="book-cover">
    <div class="wall-and-board" role="img" aria-label="White painted brick wall above a dark chessboard"></div>
    <div class="king-photo" role="img" aria-label="Photo of a gold chess king standing on the chessboard"></div>
    <h1>
      <span class="title-small">The</span>
      <span class="title-large">ORCHARD</span>
    </h1>
    <p class="subtitle">Harvest methods and the spiral<br>rising rule</p>
    <p class="author">TEODOR B. MALVEZZI</p>
  </main>
</body>
</html>
```